BQN Project Signage

Need a sign to be displayed in the front of properties currently under Construction or Renovation to advertise our company information. Need it to be Professional and Contemporary. We are a Design/Build Construction Company. Information should include Company Name, email, website, phone number. Attached: Logo and company brochure, also included and inspiration images

```html
<!DOCTYPE html>
<html lang="en">
<head>
<meta charset="utf-8">
<title>BQN Project Signage</title>
<link rel="stylesheet" href="https://fonts.googleapis.com/css2?family=Montserrat:wght@400;500;600;700&display=swap">
<style>
  :root {
    --ink: #2b2b2b;
    --ink-soft: #7a7a7a;
    --paper: #ffffff;
    --backdrop: #e9e9e7;
  }
  * { margin: 0; padding: 0; box-sizing: border-box; }
  html, body {
    width: 1200px;
    height: 1200px;
    overflow: hidden;
    background: var(--backdrop);
    font-family: "Montserrat", sans-serif;
    color: var(--ink);
  }
  .sign {
    position: absolute;
    left: 190px;
    top: 46px;
    width: 820px;
    height: 1108px;
    background: var(--ink);
    padding: 10px;
    display: flex;
    flex-direction: column;
  }
  .sign-face {
    flex: 1;
    background: var(--paper);
    display: flex;
    flex-direction: column;
    align-items: center;
    padding-top: 150px;
  }
  .brand-name {
    font-size: 46px;
    font-weight: 500;
    letter-spacing: 1px;
    text-transform: uppercase;
    color: var(--ink);
    line-height: 1;
  }
  .brand-tagline {
    margin-top: 14px;
    font-size: 30px;
    font-weight: 500;
    letter-spacing: 1px;
    text-transform: uppercase;
    color: var(--ink-soft);
    line-height: 1;
  }
  .rule {
    width: 620px;
    height: 3px;
    background: var(--ink);
  }
  .rule-top { margin-top: 56px; }
  .headline {
    margin: 22px 0 18px;
    font-size: 62px;
    font-weight: 600;
    letter-spacing: 3px;
    line-height: 1.13;
    text-align: center;
    text-transform: uppercase;
  }
  .phone {
    margin-top: 46px;
    display: flex;
    align-items: center;
    gap: 28px;
  }
  .phone-icon { width: 90px; height: 90px; }
  .phone-number {
    font-size: 82px;
    font-weight: 700;
    letter-spacing: 1px;
    line-height: 1;
  }
  .email {
    margin-top: 28px;
    font-size: 34px;
    font-weight: 500;
    letter-spacing: 2px;
  }
  .address {
    margin-top: 14px;
    font-size: 32px;
    font-weight: 500;
    letter-spacing: 1px;
    line-height: 1.25;
    text-align: center;
  }
  .footer-gap {
    height: 14px;
    background: var(--paper);
    margin-top: 10px;
  }
  .footer-band {
    height: 120px;
    display: flex;
    align-items: center;
    justify-content: center;
  }
  .website {
    color: var(--paper);
    font-size: 30px;
    font-weight: 500;
    letter-spacing: 2px;
  }
</style>
</head>
<body>
  <main class="sign">
    <section class="sign-face">
      <h1 class="brand-name">BQN Construction &amp; Design</h1>
      <p class="brand-tagline">Luxury Renovations</p>

      <div class="rule rule-top"></div>
      <h2 class="headline">High-End<br>Construction<br>&amp; Luxury<br>Renovations</h2>
      <div class="rule"></div>

      <div class="phone">
        <svg class="phone-icon" viewBox="0 0 100 100" aria-hidden="true">
          <circle cx="50" cy="50" r="50" fill="#2b2b2b"/>
          <path fill="#ffffff" d="M36 24c2-1 4 0 5 2l5 10c1 2 0 4-1 5l-4 3c2 6 8 13 15 16l3-4c1-1 3-2 5-1l10 5c2 1 3 3 2 5l-2 6c-1 3-4 5-7 5C44 75 25 56 24 33c0-3 2-6 5-7z"/>
        </svg>
        <span class="phone-number">555-014-2210</span>
      </div>

      <p class="email">INFO@BQNCONSTRUCTION.COM</p>
      <p class="address">1480 Harbor View Blvd., Ste. 310<br>Coral Point, FL 33999</p>
    </section>
    <div class="footer-gap"></div>
    <footer class="footer-band">
      <span class="website">WWW.BQNCONSTRUCTION.COM</span>
    </footer>
  </main>
</body>
</html>
```